Business card for Luxury Portable Restroom Trailer company

We are a Luxury Portable Restroom Trailer Company Called PELIKAR HIRES. Based in Orange County California. We provide portable restroom trailers for events, such as, Weddings, Concerts, Charity events, Sporting events, Tournaments, Corporate events, ect. We rent and Sell the Luxury restrooms. Our colors are white, grey, and Orange. As you will see in the logo we uploaded.
There are 2 people in the company so the names and titles will change for the 3 people but card will remain the same. Here is the information for each Person: Dennis Moyle CFO 555 018-3647
next Person: Wesley Tanford VP 555 018-3647
Next Person: Miles Tanford CEO 555 018-3647
Information to include on the card: Luxury Restroom Trailers Rental and Sales. Weddings, Concerts, Charity, Sporting and Corp. Events.

```html
<!DOCTYPE html>
<html lang="en">
<head>
<meta charset="utf-8">
<title>Pelikar Hires – Business Card</title>
<link href="https://fonts.googleapis.com/css2?family=Arimo:wght@400;700&display=swap" rel="stylesheet">
<style>
  :root {
    --backdrop: #b3b4bc;
    --card-white: #efefef;
    --card-dark: #393939;
    --pattern-tone: #333333;
    --panel-dark: #444444;
    --ink-grey: #555555;
    --brand-orange: #e0661f;
  }
  * { margin: 0; padding: 0; box-sizing: border-box; }
  html, body {
    width: 674px; height: 1200px; overflow: hidden;
    background: var(--backdrop);
    font-family: "Arimo", Arial, sans-serif;
  }
  .sheet {
    position: relative; width: 674px; height: 1200px;
    display: flex; flex-direction: column; align-items: center; justify-content: center;
    gap: 40px;
  }
  .card {
    position: relative; width: 440px; height: 251px;
    box-shadow: 0 10px 18px rgba(0,0,0,0.22);
  }
  .card--front { background: var(--card-white); color: var(--ink-grey); }
  .card--back { background: var(--card-dark); overflow: hidden; }

  .brand-name {
    font-weight: 700; letter-spacing: 0.5px; white-space: nowrap;
  }
  .card--front .brand-name {
    position: absolute; left: 37px; top: 40px;
    font-size: 19px; color: var(--ink-grey);
  }
  .tagline {
    position: absolute; right: 36px; top: 38px; text-align: right;
    font-size: 12px; line-height: 15px; text-transform: uppercase;
  }
  .tagline strong { font-weight: 700; display: block; }
  .event-list {
    position: absolute; left: 36px; top: 95px; list-style: none;
    font-size: 10.5px; text-transform: uppercase;
  }
  .event-list li { height: 27.3px; display: flex; align-items: center; }
  .event-list li::before {
    content: ""; width: 3px; height: 3px; border-radius: 50%;
    background: var(--brand-orange); margin-right: 7px;
  }
  .contact {
    position: absolute; right: 36px; top: 183px; text-align: right;
  }
  .contact-name { font-size: 14px; line-height: 18px; text-transform: uppercase; }
  .contact-name strong { color: var(--brand-orange); font-weight: 700; }
  .contact-phone {
    font-size: 13.5px; line-height: 18px;
    display: inline-flex; align-items: center; gap: 4px;
  }

  .pattern-field {
    position: absolute; inset: 0;
    background: radial-gradient(ellipse at 45% 40%, #3f3f3f, var(--pattern-tone));
  }
  .logo-panel {
    position: absolute; left: 108px; top: 93px; width: 226px; height: 67px;
    background: var(--panel-dark);
    display: flex; align-items: center; justify-content: center;
  }
  .card--back .brand-name { font-size: 23px; color: var(--brand-orange); }
</style>
</head>
<body>
<main class="sheet">
  <section class="card card--front" aria-label="Business card front">
    <div class="brand-name">PELIKAR HIRES</div>
    <p class="tagline"><strong>Luxury Restroom Trailers</strong>Rental and Sales</p>
    <ul class="event-list">
      <li>Weddings</li>
      <li>Concerts</li>
      <li>Charity</li>
      <li>Sporting</li>
      <li>And Corp. Events</li>
    </ul>
    <div class="contact">
      <p class="contact-name"><strong>Dennis Moyle</strong> CFO</p>
      <p class="contact-phone">
        <svg width="8" height="11" viewBox="0 0 8 11" aria-hidden="true">
          <rect x="0.75" y="0.75" width="6.5" height="9.5" rx="1.2" fill="none" stroke="currentColor" stroke-width="1.4"/>
          <rect x="2.5" y="8" width="3" height="0.9" fill="currentColor"/>
        </svg>
        555 018-3647
      </p>
    </div>
  </section>

  <section class="card card--back" aria-label="Business card back">
    <div class="pattern-field" role="img" aria-label="Embossed repeating brand emblem pattern in dark grey"></div>
    <div class="logo-panel">
      <div class="brand-name">PELIKAR HIRES</div>
    </div>
  </section>
</main>
</body>
</html>
```